Tabloid Magazine Flyer Class Action Lawsuit

Create a bold, 2-page 8.5" x 11" flyer with the look and feel of a tabloid exposé — loud, sensational, and impossible to ignore. Use bold fonts, dramatic headlines, and high-contrast colors (red, black, white, deep blue). Fill every inch of space — no white space, no subtlety. Use the provided images prominently. Page 1 should grab attention with a shocking headline, impactful image, and strong call to action. Page 2 should stack bold subheadings and explosive bullet points. Emphasize urgency, outrage, and grassroots power. This flyer is meant to rally a community.
Updates

Need to extend because we haven't received a design that meets our needs

Target Market(s)

All instructions and content are in the attached word doc

Industry/Entity Type

Requirements
Must have
• All instructions and content are in the attached word doc
Nice to have
Should not have

```html
<!DOCTYPE html>
<html lang="en">
<head>
<meta charset="utf-8">
<title>Harbor Park Exposed – Flyer</title>
<link href="https://fonts.googleapis.com/css2?family=Montserrat:wght@500;700;800;900&family=Open+Sans:wght@400;600;700&display=swap" rel="stylesheet">
<style>
:root{
  --red:#d2233c;
  --deep-red:#a81b3a;
  --navy:#1c2a72;
  --purple:#3b2c8a;
  --bright-blue:#2f6fd8;
  --yellow:#ffd21f;
  --white:#ffffff;
  --ink:#111827;
  --paper:#ffffff;
}
*{box-sizing:border-box;margin:0;padding:0}
html,body{width:1200px;height:1188px;overflow:hidden;background:var(--paper)}
body{position:relative;font-family:"Open Sans",Arial,sans-serif;color:var(--white)}
.side-label{position:absolute;font-family:"Montserrat",Arial,sans-serif;font-weight:800;font-size:26px;color:var(--ink);letter-spacing:1px}
.side-label--front{left:262px;top:44px}
.side-label--back{left:842px;top:220px}

.page{position:absolute;overflow:hidden;box-shadow:0 6px 18px rgba(0,0,0,.35)}

/* FRONT */
.front{left:28px;top:105px;width:630px;height:800px;z-index:2;
  background:linear-gradient(165deg,var(--purple) 0%,var(--red) 26%,var(--deep-red) 44%,#5a2a80 68%,var(--navy) 100%)}
.headline{position:absolute;left:28px;top:62px;font-family:"Montserrat",Arial,sans-serif;font-weight:900;line-height:.94;text-transform:uppercase}
.headline span{display:block}
.headline .w{font-size:54px;color:var(--white)}
.headline .y{font-size:96px;color:var(--yellow);letter-spacing:-2px}
.shock{position:absolute;left:28px;top:288px;width:312px;font-family:"Montserrat",Arial,sans-serif;font-weight:800;font-size:24px;line-height:1.12;text-transform:uppercase}
.fight-box{position:absolute;left:0;top:408px;width:300px;padding:8px 28px;background:var(--bright-blue);font-family:"Montserrat",Arial,sans-serif;font-weight:700;font-size:19px;line-height:1.2}
.public-note{position:absolute;left:28px;top:484px;width:290px;font-size:16px;line-height:1.3;font-weight:600}
.event{position:absolute;left:332px;top:18px;width:284px}
.event .invite{font-family:"Montserrat",Arial,sans-serif;font-weight:700;font-size:24px;line-height:1.15}
.event .venue{margin-top:8px;font-family:"Montserrat",Arial,sans-serif;font-weight:800;font-size:23px;line-height:1.12;color:var(--yellow);text-transform:uppercase}
.detail{display:flex;align-items:flex-start;gap:12px;margin-top:18px;font-family:"Montserrat",Arial,sans-serif;font-weight:700;font-size:18px;line-height:1.2}
.detail svg{flex:0 0 24px;margin-top:-1px}
.rally{position:absolute;left:332px;top:420px;width:284px;font-family:"Montserrat",Arial,sans-serif;font-weight:800;font-size:17px;line-height:1.35;text-transform:uppercase}
.url-pill{position:absolute;left:44px;top:562px;width:542px;height:48px;border-radius:24px;background:var(--white);color:var(--navy);font-family:"Montserrat",Arial,sans-serif;font-weight:900;font-size:34px;display:flex;align-items:center;justify-content:center}
.lawsuit-strip{position:absolute;left:0;bottom:0;width:100%;height:165px;background:var(--white);color:var(--ink);padding:22px 18px}
.lawsuit-strip h3{font-family:"Montserrat",Arial,sans-serif;font-weight:900;font-size:16px;color:var(--red)}
.lawsuit-strip p{width:350px;margin-top:8px;font-size:10.5px;line-height:1.4;font-weight:600}
.partner-name{position:absolute;right:20px;top:28px;display:flex;align-items:center;gap:8px;width:180px;font-family:"Montserrat",Arial,sans-serif;font-weight:800;font-size:17px;color:var(--red);line-height:1.15}
.partner-name i{flex:0 0 22px;height:22px;border-radius:50%;background:var(--navy)}

/* BACK */
.back{left:585px;top:260px;width:585px;height:760px;z-index:1;
  background:linear-gradient(180deg,var(--navy) 0%,#2c2a84 40%,var(--purple) 70%,#4a2a82 100%)}
.back-hero{position:absolute;left:0;top:0;width:100%;height:115px;background:linear-gradient(110deg,var(--deep-red),#5a2a80 55%,var(--navy))}
.hero-photo{position:absolute;right:0;top:0;width:180px;height:115px;background:linear-gradient(160deg,#7fb3e6,#c44a5a 60%,#2a2f7a)}
.tag{position:absolute;left:92px;top:8px;background:var(--red);font-family:"Montserrat",Arial,sans-serif;font-weight:900;font-size:12px;padding:2px 8px}
.hero-text{position:absolute;left:92px;top:30px;width:300px;font-size:9px;line-height:1.4}
.hero-text b{font-family:"Montserrat",Arial,sans-serif;font-size:14px;color:var(--yellow);display:block;margin-bottom:2px}
.back h2{position:absolute;left:92px;top:124px;font-family:"Montserrat",Arial,sans-serif;font-weight:900;font-size:18px;color:var(--yellow)}
.facts{position:absolute;left:92px;top:156px;width:470px}
.fact{margin-bottom:12px;font-size:9.5px;line-height:1.4}
.fact h4{font-family:"Montserrat",Arial,sans-serif;font-weight:800;font-size:9.5px;color:#ff5b6e;text-transform:uppercase;margin-bottom:2px}
.fact--narrow p{width:295px}
.fact-photo{position:absolute;left:405px;top:208px;width:160px;height:80px;background:linear-gradient(180deg,#7aa6d8,#2f5fb0)}
.back-url{position:absolute;left:120px;top:664px;width:340px;height:28px;border-radius:14px;background:var(--white);color:var(--navy);font-family:"Montserrat",Arial,sans-serif;font-weight:900;font-size:18px;display:flex;align-items:center;justify-content:center}
.back-strip{position:absolute;left:0;bottom:0;width:100%;height:60px;background:var(--white);padding:12px 0 0 92px}
.back-strip p{font-family:"Montserrat",Arial,sans-serif;font-weight:900;font-size:12px;line-height:1.4;color:var(--red)}
.back-strip p+p{color:var(--navy)}
.badge{position:absolute;top:13px;width:34px;height:34px}
.badge--a{right:52px;background:var(--bright-blue)}
.badge--b{right:12px;border-radius:50%;background:var(--red)}
</style>
</head>
<body>
<div class="side-label side-label--front">FRONT</div>
<div class="side-label side-label--back">BACK</div>

<section class="page back">
  <div class="back-hero">
    <div class="tag">EXPOSED</div>
    <p class="hero-text"><b>Marco Vellani</b>CEO of Ridgeline Asset Pool LLC is the leaseholder of Harbor Park. Residents say his company has profited from public land while ignoring the city, the lease terms, our peace, and our environment — all from his seaside office.</p>
    <div class="hero-photo" role="img" aria-label="Photo of the leaseholder at a crowded beach event"></div>
  </div>
  <h2>WHAT THEY DON'T WANT YOU TO KNOW:</h2>
  <div class="fact-photo" role="img" aria-label="Photo of portable toilets lined up near the beach"></div>
  <div class="facts">
    <div class="fact"><h4>Illegal raves — no permits</h4><p>Explosive amplified concerts ran past midnight week after week, with no permits. City records show no event permits and no council approval.</p></div>
    <div class="fact fact--narrow"><h4>The beach house isn't theirs — it's yours</h4><p>Harbor Park sits on public land leased by the city. Our lease payments fund the public, not private parties. The land, the boardwalk, and the beach belong to every resident.</p></div>
    <div class="fact fact--narrow"><h4>Disabled child traumatized by rave noise</h4><p>A child with sensory needs was harmed by repeated noise at levels far beyond city limits. Families filed complaints for months. Nothing changed.</p></div>
    <div class="fact"><h4>Exposed: is Harbor Park running a self-dealing scheme?</h4><p>Filings show the same owners on both sides of key contracts. Revenue meant for upkeep appears to flow to related private companies.</p></div>
    <div class="fact"><h4>Documented injury and suspected environmental damage</h4><p>Crowds trampled dunes and left trash on the sand. Portable toilets leaked near storm drains that empty straight into the bay.</p></div>
    <div class="fact"><h4>Exposed: did illegal raves block the public?</h4><p>Gates, fences and paid wristbands kept locals off public walkways during events. The lease requires open access at all times.</p></div>
    <div class="fact"><h4>Harbor Park accountability starts now</h4><p>From the boardwalk to the arcade, residents demand a full audit, an independent review, and real penalties for every broken lease term.</p></div>
  </div>
  <div class="back-url">www.FixHarborPark.org</div>
  <div class="back-strip">
    <p>HELP OUR COMMUNITY SAVE HARBOR PARK</p>
    <p>HARBOR PARK WAS BUILT FOR FAMILIES — NOT RAVES</p>
    <span class="badge badge--a"></span>
    <span class="badge badge--b"></span>
  </div>
</section>

<section class="page front">
  <h1 class="headline"><span class="w">Harbor</span><span class="y">Park</span><span class="w">Exposed</span></h1>
  <p class="shock">Disabled child traumatized public land abused for profit</p>
  <div class="fight-box">Help Our Beach Community Fight Back</div>
  <p class="public-note">Harbor park is not private. It is public property Owned by the city, paid for by you.</p>

  <div class="event">
    <p class="invite">Join us &amp; show your support @</p>
    <p class="venue">Seacrest Beach Town Council Meeting</p>
    <div class="detail">
      <svg width="24" height="24" viewBox="0 0 26 26"><rect x="2" y="4" width="22" height="20" rx="3" fill="#ffd21f"/><rect x="2" y="4" width="22" height="6" fill="#d2233c"/><rect x="7" y="1" width="3" height="6" fill="#fff"/><rect x="16" y="1" width="3" height="6" fill="#fff"/></svg>
      <span>May 14, 2025</span>
    </div>
    <div class="detail">
      <svg width="24" height="24" viewBox="0 0 26 26"><circle cx="13" cy="13" r="11" fill="#ffd21f"/><path d="M13 6v7l5 3" stroke="#1c2a72" stroke-width="2.5" fill="none" stroke-linecap="round"/></svg>
      <span>6:00 PM</span>
    </div>
    <div class="detail">
      <svg width="24" height="24" viewBox="0 0 26 26"><path d="M13 1c-5 0-9 4-9 9 0 7 9 15 9 15s9-8 9-15c0-5-4-9-9-9z" fill="#ffd21f"/><circle cx="13" cy="10" r="3.5" fill="#d2233c"/></svg>
      <span>Harbor Park Community Room (Above The Arcade)</span>
    </div>
  </div>
  <p class="rally">Help our community save Harbor Park Harbor Park was built for families — not raves</p>

  <div class="url-pill">www.FixHarborPark.org</div>

  <div class="lawsuit-strip">
    <h3>CLASS ACTION LAWSUIT FORMING NOW!</h3>
    <p>If You've Been Impacted By Noise, Denied Public Access, Or Harmed By These Violations, You May Be Eligible For Compensation. We're Gathering Stories And Preparing Legal Action.</p>
    <div class="partner-name"><i></i>Equal Access Coalition</div>
  </div>
</section>
</body>
</html>
```